Harlowe Skid Service Business Cards

WHAT WE DOWe RepairWe CustomizeWe ManufactureWe Deliver
Reason: Hello,
I would like to extend the deadline to May 1st - no additional fee. Reason being is because I am waiting on a reply from feedback from the designed that we are planning on choosing. I would like an answer as soon as possible, please and thanks!!!
Industry/Entity Type
Business
Contact Information for Business Card
Mireya Quintanal
Vice President
Office: 847-555-0142
Cell: 708-555-0187
Fax: 847-555-0163
mireya@harloweskid.com
Harlowe Skid Service II, Inc
2290 Fernhollow Avenue
Oak Briar Village, IL 60094
www.harloweskid.com
Look and feel
Each slider illustrates characteristics of the customer's brand and the style your logo design should communicate.

```html
<!DOCTYPE html>
<html lang="en">
<head>
<meta charset="utf-8">
<title>Harlowe Skid Service Business Cards</title>
<link href="https://fonts.googleapis.com/css2?family=Source+Sans+3:wght@400;600;700&display=swap" rel="stylesheet">
<style>
  :root {
    --brand-red: #ee3535;
    --ink-grey: #555555;
    --card-white: #ffffff;
    --stage-top: #2a2a2a;
    --stage-bottom: #050505;
  }
  * { margin: 0; padding: 0; box-sizing: border-box; }
  html, body { width: 1200px; height: 900px; overflow: hidden; }
  body {
    background: linear-gradient(180deg, var(--stage-top) 0%, #151515 55%, var(--stage-bottom) 100%);
    font-family: "Source Sans 3", "Myriad Pro", sans-serif;
    position: relative;
  }
  .card {
    position: absolute;
    top: 306px;
    width: 440px;
    height: 271px;
    border-radius: 10px;
  }
  .card-front { left: 149px; background: var(--card-white); }
  .card-back { left: 608px; background: var(--brand-red); color: var(--card-white); }

  .brand-name-front {
    position: absolute;
    left: 29px;
    top: 110px;
    font-size: 23px;
    font-weight: 600;
    color: var(--brand-red);
    white-space: nowrap;
  }

  .contact {
    position: absolute;
    left: 264px;
    top: 60px;
    color: var(--ink-grey);
    font-size: 12.5px;
    line-height: 15px;
    white-space: nowrap;
  }
  .contact-name { color: var(--brand-red); font-size: 15.5px; font-weight: 600; line-height: 18px; }
  .contact-title { margin-bottom: 9px; }
  .contact-company { color: var(--brand-red); font-weight: 700; font-size: 12.5px; margin-bottom: 5px; }
  .contact-address { margin-bottom: 11px; }
  .phone-line { display: flex; align-items: center; gap: 6px; height: 16px; }
  .phone-line svg { width: 10px; height: 10px; fill: var(--brand-red); flex: none; }

  .brand-name-back {
    position: absolute;
    left: 0; right: 0;
    top: 84px;
    text-align: center;
    font-size: 40px;
    font-weight: 700;
    letter-spacing: 0.5px;
  }
  .services-heading {
    position: absolute;
    left: 0; right: 0;
    top: 195px;
    text-align: center;
    font-size: 13.5px;
    font-weight: 700;
  }
  .services-list {
    position: absolute;
    left: 0; right: 0;
    top: 217px;
    text-align: center;
    font-size: 14.5px;
  }
</style>
</head>
<body>
  <section class="card card-front">
    <div class="brand-name-front">Harlowe Skid Service</div>
    <div class="contact">
      <div class="contact-name">Mireya Quintanal</div>
      <div class="contact-title">Vice President</div>
      <div class="contact-company">Harlowe Skid Service II, Inc</div>
      <div class="contact-address">2290 Fernhollow Avenue<br>Oak Briar Village, IL 60094</div>
      <div class="phone-line">
        <svg viewBox="0 0 10 10" aria-hidden="true"><path d="M2 0.5 L3.6 2.6 L2.8 3.6 Q3.8 5.6 6.4 7.2 L7.4 6.4 L9.5 8 L8.4 9.5 Q4.5 9.2 0.5 1.6 Z"/></svg>
        <span>847-555-0142</span>
      </div>
      <div class="phone-line">
        <svg viewBox="0 0 10 10" aria-hidden="true"><path d="M2.5 0 H7.5 V10 H2.5 Z M3.5 1.5 V7.5 H6.5 V1.5 Z"/></svg>
        <span>708-555-0187</span>
      </div>
      <div class="phone-line">
        <svg viewBox="0 0 10 10" aria-hidden="true"><path d="M3 0.5 H7 V3 H9.5 V9.5 H0.5 V3 H3 Z M4 1.5 V3 H6 V1.5 Z M2 5 V6 H4 V5 Z M5 5 V6 H8 V5 Z"/></svg>
        <span>847-555-0163</span>
      </div>
    </div>
  </section>

  <section class="card card-back">
    <div class="brand-name-back">Harlowe Skid Service</div>
    <div class="services-heading">WHAT WE DO</div>
    <div class="services-list">We Repair | We Customize | We Manufacture | We Deliver</div>
  </section>
</body>
</html>
```